Business Card Design for Logistics Startup

Link to my logo source file -
https://www.filecrate-demo.net/sh/qx7vmp2lr9kdwta/BBTzY4_LQm8hRuPoKvxVc?dl=0

We want a statement in our business card!
I have go thru your portfolio, and invites 3 of you guys to design my business card as the previous designer cannot give me the feel.
Let me know if you want any information.
Thanks.

Target Market(s)

Transport and Logistics
: Shippers, Freight Forwarders and Carriers.

Industry/Entity Type

Business

Contact Information for Business Card

Our details;

Name: Marcus Lim
Designation: General Manager
Mobile: +65 93415062
Email: marcus.lim@korvanth.com
Address: 7 Jalan Merpati Rise
TRINOX Plaza #03-17
Singapore 612379

Name: Daniel Ho
Designation: Director
Mobile: +65 97264318
Email: daniel.ho@korvanth.com
TRINOX Plaza #03-17
Singapore 612379

Colors
f37122

Requirements
Must have
• Logo from my source file.
• Please included tagline: Transport and Logistics
• If you guy can think of a tagline - Using E and S, that will be perfect. Such as Excellence in Service..

```html
<!DOCTYPE html>
<html lang="en">
<head>
<meta charset="utf-8">
<title>Korvanth Business Card</title>
<link href="https://fonts.googleapis.com/css2?family=Hind:wght@300;400;500;600&display=swap" rel="stylesheet">
<style>
  :root {
    --brand-orange: #e36512;
    --ink: #1e1e1e;
    --paper: #ffffff;
    --backdrop: #e8e8e8;
  }
  * { box-sizing: border-box; margin: 0; padding: 0; }
  html, body {
    width: 1200px; height: 900px; overflow: hidden;
    background: var(--backdrop);
    font-family: "Hind", sans-serif;
  }
  .card {
    position: absolute; left: 382px;
    width: 411px; height: 253px;
  }
  .card--front { top: 147px; background: var(--paper); color: var(--ink); }
  .card--back { top: 473px; background: var(--brand-orange); color: var(--paper); }

  .brand-lockup {
    position: absolute; left: 27px; top: 31px;
    display: flex; align-items: center; gap: 14px;
  }
  .brand-mark {
    width: 50px; height: 50px;
    border: 3px solid var(--brand-orange);
  }
  .brand-name {
    font-size: 17px; font-weight: 500; letter-spacing: 3px;
    color: var(--ink);
  }

  .holder { position: absolute; left: 27px; top: 118px; }
  .holder-name { font-size: 15px; font-weight: 600; color: var(--brand-orange); line-height: 1.2; }
  .holder-role { font-size: 11px; font-weight: 400; letter-spacing: 0.3px; line-height: 1.5; }

  .contact-list {
    position: absolute; left: 27px; top: 177px;
    list-style: none; font-size: 11px; line-height: 14px;
  }
  .contact-list li { display: flex; align-items: center; gap: 5px; }
  .contact-icon { width: 10px; height: 10px; fill: var(--brand-orange); }

  .address {
    position: absolute; right: 28px; top: 177px;
    font-style: normal; font-size: 11px; line-height: 14px; text-align: right;
  }
  .rule {
    position: absolute; left: 27px; right: 28px; top: 222px;
    height: 1px; background: var(--brand-orange);
  }

  .back-lockup {
    position: absolute; left: 0; right: 0; top: 48px;
    display: flex; flex-direction: column; align-items: center;
  }
  .back-mark {
    width: 56px; height: 56px; border-radius: 50%;
    border: 2px solid var(--paper);
  }
  .back-name {
    margin-top: 12px; font-size: 19px; font-weight: 500; letter-spacing: 4px;
  }
  .back-sector {
    margin-top: 4px; font-size: 8px; font-weight: 400; letter-spacing: 2.5px;
  }
  .tagline {
    position: absolute; left: 0; right: 0; top: 221px;
    text-align: center; font-size: 13px; font-weight: 300;
  }
</style>
</head>
<body>
  <section class="card card--front">
    <div class="brand-lockup">
      <div class="brand-mark"></div>
      <span class="brand-name">KORVANTH</span>
    </div>

    <div class="holder">
      <p class="holder-name">Daniel Ho</p>
      <p class="holder-role">DIRECTOR</p>
    </div>

    <ul class="contact-list">
      <li>
        <svg class="contact-icon" viewBox="0 0 10 10" aria-hidden="true"><path d="M3 0h4a1 1 0 0 1 1 1v8a1 1 0 0 1-1 1H3a1 1 0 0 1-1-1V1a1 1 0 0 1 1-1zm0 1.5v6h4v-6zM5 8.2a.5.5 0 1 0 0 1 .5.5 0 0 0 0-1z"/></svg>
        +65 9726 4318
      </li>
      <li>
        <svg class="contact-icon" viewBox="0 0 10 10" aria-hidden="true"><path d="M0 2h10v.6L5 5.6 0 2.6zM0 3.6l5 3 5-3V8H0z"/></svg>
        daniel.ho@korvanth.com
      </li>
      <li>
        <svg class="contact-icon" viewBox="0 0 10 10" aria-hidden="true"><circle cx="5" cy="5" r="4.5"/><path d="M2.5 3.5c1-.3 1.8.3 1.6 1.2-.2.8.9 1 .6 2-.2.6-.2 1.2.3 1.6" stroke="#fff" stroke-width="1" fill="none"/></svg>
        www.korvanth.com
      </li>
    </ul>

    <address class="address">
      7 Jalan Merpati Rise<br>
      TRINOX Plaza #03-17<br>
      Singapore 612379
    </address>

    <div class="rule"></div>
  </section>

  <section class="card card--back">
    <div class="back-lockup">
      <div class="back-mark"></div>
      <span class="back-name">KORVANTH</span>
      <span class="back-sector">TRANSPORT &amp; LOGISTICS</span>
    </div>
    <p class="tagline">Every Load Moved. Every Promise Kept.</p>
  </section>
</body>
</html>
```